BrightNomadRx.com Blog Design (Travel, Lifestyle, and Life Hacking blog)

I am launching a lifestyle blog about my life. I'm a doctor who travels the world trying the best restaurants, airlines and trying to have as much fun as possible. I also invest in startups, and am always trying new tricks to make life better. I also plan to write about various other topics, but essentially it is about travel, lifestyle and medicine. I need a creative and really awesome looking design for a new wordpress blog called BrightNomadRx

Target Market(s)

Physicians, Entrepreneurs, Travellers

Industry/Entity Type

Airlines

Number of Pages Required

1 page

Font styles to use
Serif

Requirements
Must have
• Slick looking graphics with a highly professional modern feel

```html
<!DOCTYPE html>
<html lang="en">
<head>
<meta charset="utf-8">
<title>BrightNomadRx — Travel, Lifestyle &amp; Medicine Blog</title>
<link rel="stylesheet" href="https://fonts.googleapis.com/css2?family=Josefin+Sans:wght@400;600;700&family=Oswald:wght@400;500&display=swap">
<style>
:root{
  --ink:#222;
  --ink-soft:#555;
  --muted:#8a8a8a;
  --bar:#111;
  --nav:#2c2c2c;
  --hero-bg:#e6e6e6;
  --panel:#efefef;
  --panel-dark:#333;
  --cyan:#2bb5d8;
  --red:#f04b4b;
  --orange:#f7a21b;
  --green:#6cb33f;
  --read:#f26b3a;
  --footer:#222;
  --white:#fff;
}
*{box-sizing:border-box;margin:0;padding:0}
html,body{width:1200px;height:3991px;overflow:hidden;background:var(--white)}
body{font-family:"Josefin Sans",Arial,sans-serif;color:var(--ink);position:relative}

/* top bar */
.top-bar{position:absolute;left:0;top:0;width:1200px;height:58px;background:var(--bar)}
.brand{position:absolute;left:72px;top:14px;color:var(--white);font-family:"Josefin Sans",sans-serif;font-weight:700;font-size:30px;letter-spacing:.5px}
.top-social{position:absolute;right:72px;top:17px;display:flex;gap:6px}
.top-social span{width:24px;height:24px;border:1px solid #666;border-radius:50%}

/* nav */
.main-nav{position:absolute;left:0;top:58px;width:1200px;height:48px;background:var(--nav)}
.main-nav ul{list-style:none;display:flex;position:absolute;left:75px;top:0;height:48px}
.main-nav li{color:var(--white);font-size:15px;font-weight:600;text-transform:uppercase;padding:0 13px;line-height:50px}
.main-nav li.active{background:var(--red)}
.search{position:absolute;right:75px;top:9px;width:298px;height:30px;background:#444;color:#ccc;font-size:13px;padding:8px 10px}
.search svg{position:absolute;right:9px;top:7px}

/* hero */
.hero{position:absolute;left:0;top:106px;width:1200px;height:564px;background:var(--hero-bg)}
.hero-card{position:absolute;overflow:hidden}
.hero-card .photo{position:absolute;inset:0}
.hero-card .cat{position:absolute;right:0;top:0;color:var(--white);font-size:14px;font-weight:600;padding:6px 10px 3px;text-transform:uppercase}
.hero-card h2{position:absolute;left:18px;right:18px;bottom:14px;color:var(--white);font-weight:400;font-size:22px;line-height:1.2;text-transform:uppercase}

/* section heads */
.sec-head{position:absolute;height:32px;border-bottom:3px solid var(--c)}
.sec-head .tag{position:absolute;left:0;top:0;height:29px;background:var(--c);color:var(--white);font-size:16px;font-weight:600;text-transform:uppercase;padding:8px 10px 0;white-space:nowrap}
.sec-head .more{position:absolute;right:0;top:7px;height:16px;background:#333;color:var(--white);font-size:10px;font-weight:700;padding:3px 7px 0}

/* feature cards */
.feature{position:absolute;width:343px;height:295px;overflow:hidden}
.feature .photo{position:absolute;inset:0}
.feature .badge{position:absolute;top:182px;left:50%;transform:translateX(-50%);background:var(--red);color:var(--white);font-size:10px;font-weight:700;padding:4px 8px 2px}
.feature h3{position:absolute;left:20px;right:20px;top:203px;text-align:center;color:var(--white);font-family:"Oswald",sans-serif;font-weight:500;font-size:18px;line-height:1.25}
.feature .meta{position:absolute;left:0;right:0;top:255px;text-align:center;color:#eee;font-size:11px}

/* small list */
.mini{position:absolute;width:349px;height:80px}
.mini .thumb{position:absolute;left:0;top:0;width:125px;height:80px}
.mini h4{position:absolute;left:137px;top:2px;width:210px;font-size:15px;font-weight:600;line-height:1.3}
.mini .meta{position:absolute;left:137px;top:48px;font-size:10px;color:var(--muted);white-space:nowrap}
.mini.narrow{width:343px}
.mini.narrow .thumb{width:120px}
.mini.narrow h4,.mini.narrow .meta{left:135px}
.mini.narrow h4{width:208px}

/* recent posts */
.post{position:absolute;left:75px;width:705px;height:160px}
.post .thumb{position:absolute;left:0;top:0;width:231px;height:155px}
.post .cat{position:absolute;left:6px;top:6px;color:var(--white);font-size:11px;font-weight:600;padding:4px 7px 2px;text-transform:uppercase}
.post h4{position:absolute;left:247px;top:2px;font-size:15px;font-weight:600;white-space:nowrap}
.post .meta{position:absolute;left:247px;top:30px;font-size:10px;color:var(--muted);white-space:nowrap}
.post p{position:absolute;left:247px;top:52px;width:450px;font-size:13px;line-height:1.45;color:var(--ink-soft)}
.post .read{position:absolute;left:247px;top:114px;background:var(--read);color:var(--white);font-size:11px;font-weight:700;padding:6px 9px 3px}

.pager{position:absolute;left:75px;top:2676px;font-size:13px;font-weight:700;color:#444;letter-spacing:.5px}

/* sidebar */
.side-box{position:absolute;left:793px;width:333px}
.about{top:718px;height:421px;background:var(--panel-dark);color:#ddd;text-align:center}
.avatar{position:absolute;left:108px;top:36px;width:118px;height:118px;border-radius:50%;background:linear-gradient(160deg,#e9e9e9,#c7cfd6);border:4px solid var(--white)}
.about p{position:absolute;left:28px;right:28px;top:176px;font-size:13px;line-height:1.5}
.about .btn{position:absolute;left:110px;top:348px;border:1px solid #bbb;color:var(--white);font-size:11px;font-weight:700;padding:8px 14px 5px}

.social-grid{position:absolute;left:793px;top:1203px;width:333px;display:grid;grid-template-columns:1fr 1fr;gap:6px}
.social-grid div{height:64px;color:var(--white);position:relative;padding:12px 0 0 56px;font-size:11px;line-height:1.4;text-transform:uppercase}
.social-grid div::before{content:"";position:absolute;left:14px;top:16px;width:30px;height:30px;border:2px solid rgba(255,255,255,.7);border-radius:4px}
.social-grid b{display:block;font-size:14px}

.ad{position:absolute;left:820px;top:1445px;width:279px;height:279px;background:#f4f1ec;overflow:hidden}
.ad .watch{position:absolute;left:0;top:0;width:130px;height:279px;background:linear-gradient(160deg,#7a2320,#b3473b 55%,#5a1a18)}
.ad .kicker{position:absolute;left:140px;right:8px;top:22px;text-align:center;font-size:14px;letter-spacing:2px;color:#444}
.ad .title{position:absolute;left:140px;right:8px;top:44px;text-align:center;font-size:22px;font-weight:700;line-height:1.05;color:#333}
.ad .name{position:absolute;left:140px;right:8px;top:128px;text-align:center;font-size:18px;font-weight:700;color:#333}
.ad .shop{position:absolute;left:158px;top:200px;background:#3aa8a4;color:var(--white);font-size:13px;font-weight:700;padding:7px 12px 4px}
.ad .url{position:absolute;left:140px;right:8px;top:248px;text-align:center;font-size:10px;color:#555}

.news{top:1788px;height:226px;background:var(--panel)}
.news p{position:absolute;left:14px;right:14px;top:16px;font-size:13px;line-height:1.45;color:var(--ink-soft)}
.field{position:absolute;left:14px;width:300px;height:36px;background:var(--white);border:1px solid #ddd;font-size:12px;color:#666;padding:12px 10px 0}
.news .sub{position:absolute;left:14px;top:166px;width:300px;height:38px;background:var(--red);color:var(--white);text-align:center;font-size:14px;font-weight:700;padding-top:13px}

.tweets{top:2076px;height:255px;background:var(--panel);text-align:center}
.tweets .bird{position:absolute;left:150px;top:20px}
.tweets p{position:absolute;left:20px;right:20px;top:70px;font-size:14px;line-height:1.5;color:#444}
.tweets .link{color:var(--cyan)}
.tweets .date{position:absolute;left:0;right:0;top:140px;font-size:11px;color:#666}
.tweets .acts{position:absolute;left:0;right:0;top:168px;font-size:13px;color:var(--cyan)}
.dots{position:absolute;left:143px;top:208px;display:flex;gap:6px}
.dots i{width:6px;height:6px;border-radius:50%;background:#bbb}
.dots i:first-child{background:var(--cyan)}

.archive{top:2400px;list-style:none}
.archive li{height:37px;font-size:13px;color:#444;padding-left:22px;position:relative;border-bottom:1px solid #eee;padding-top:12px}
.archive li::before{content:"";position:absolute;left:6px;top:14px;width:7px;height:7px;border-radius:50%;background:var(--cyan)}

.photo-feed{top:2688px;height:439px;background:var(--panel)}
.photo-feed .grid{position:absolute;left:38px;top:20px;width:262px;display:grid;grid-template-columns:repeat(3,1fr);gap:6px}
.photo-feed .grid div{height:82px}
.photo-feed .btn{position:absolute;left:38px;top:386px;width:262px;height:32px;background:var(--white);border:1px solid #999;text-align:center;font-size:12px;padding-top:10px;color:#333}

/* footer */
.footer{position:absolute;left:0;top:3805px;width:1200px;height:186px;background:var(--footer);color:#ccc;text-align:center}
.footer nav{position:absolute;left:0;right:0;top:34px;font-size:13px;text-transform:uppercase;letter-spacing:.3px}
.footer nav span{margin:0 6px;color:#888}
.footer .icons{position:absolute;left:0;right:0;top:82px;display:flex;justify-content:center;gap:6px}
.footer .icons i{width:28px;height:28px;border:2px solid #aaa;border-radius:50%}
.footer .copy{position:absolute;left:0;right:0;top:150px;font-size:12px;color:#999}

/* tones */
.t-mountain{background:linear-gradient(180deg,#9fb3c4 0%,#c8d3dc 45%,#6f7d88 80%,#4b4a46 100%)}
.t-couple{background:linear-gradient(160deg,#c9a27f,#e3c2a0 40%,#8f6a4e 100%)}
.t-laptop{background:linear-gradient(180deg,#0f2233,#2b4c66 60%,#10202e)}
.t-fruit{background:linear-gradient(150deg,#7a8c5e,#c8472f 50%,#e6a13a 80%,#6a7a4d)}
.t-beach{background:linear-gradient(180deg,#8fc7e8 0%,#d8e6ee 55%,#d9b98c 78%,#8b6b45 100%)}
.t-lake{background:linear-gradient(180deg,#79b6d6,#3f8fb3 55%,#5d6a4a)}
.t-boat{background:linear-gradient(180deg,#a8dbe8,#2fa6b8 60%,#e0d3b0)}
.t-field{background:linear-gradient(180deg,#e8d6a6,#c79d5a 60%,#7c6236)}
.t-curly{background:linear-gradient(150deg,#bfc8d0,#8a6a52 45%,#d7c0a6)}
.t-pills{background:linear-gradient(160deg,#e8e2dd,#9fb9c9 40%,#c24a3b 70%,#5d6f7e)}
.t-clinic{background:linear-gradient(160deg,#e5ecf0,#b9c7cf 60%,#8aa3b2)}
.t-salad{background:linear-gradient(150deg,#f0eee6,#8fb35a 50%,#d45c3b)}
.t-bike{background:linear-gradient(180deg,#cfe3ee,#9cb8c6 50%,#6d7a64)}
.t-friends{background:linear-gradient(160deg,#c78e5a,#5f3f2a 60%,#2d2b2a)}
</style>
</head>
<body>

<header class="top-bar">
  <div class="brand">BrightNomadRx</div>
  <div class="top-social"><span></span><span></span><span></span><span></span><span></span><span></span><span></span></div>
</header>

<nav class="main-nav">
  <ul>
    <li class="active">Home</li><li>About Us</li><li>Travel</li><li>Lifestyle</li><li>Life Hacking</li><li>Medicine</li><li>Contact</li>
  </ul>
  <div class="search">Search
    <svg width="16" height="16" viewBox="0 0 16 16"><circle cx="6.5" cy="6.5" r="5" fill="none" stroke="#ccc" stroke-width="2"/><line x1="10.5" y1="10.5" x2="15" y2="15" stroke="#ccc" stroke-width="2"/></svg>
  </div>
</nav>

<section class="hero">
  <article class="hero-card" style="left:75px;top:27px;width:423px;height:506px">
    <div class="photo t-mountain" role="img" aria-label="Hiker with backpack standing on a mountain peak above the clouds"></div>
    <span class="cat" style="background:var(--green)">Travel</span>
    <h2>Lorem ipsum dolor sit amet, consectetur adipiscing</h2>
  </article>
  <article class="hero-card" style="left:506px;top:27px;width:252px;height:506px">
    <div class="photo t-couple" role="img" aria-label="Smiling couple outdoors"></div>
    <span class="cat" style="background:var(--red)">Life Style</span>
    <h2>Lorem ipsum dolor sit amet</h2>
  </article>
  <article class="hero-card" style="left:766px;top:27px;width:360px;height:250px">
    <div class="photo t-laptop" role="img" aria-label="Person working on a laptop in a dark room"></div>
    <span class="cat" style="background:var(--green)">Life Hacking</span>
    <h2>Lorem ipsum dolor sit amet, consectetur</h2>
  </article>
  <article class="hero-card" style="left:766px;top:285px;width:360px;height:248px">
    <div class="photo t-fruit" role="img" aria-label="Fresh fruit and vegetables arranged in a heart-shaped bowl with a stethoscope"></div>
    <span class="cat" style="background:var(--orange)">Medicine</span>
    <h2>Lorem ipsum dolor sit amet, consectetur</h2>
  </article>
</section>

<!-- Travel block -->
<div class="sec-head" style="--c:var(--cyan);left:75px;top:687px;width:705px"><span class="tag">Travel</span><span class="more">MORE ›</span></div>
<article class="feature" style="left:75px;top:737px">
  <div class="photo t-beach" role="img" aria-label="Woman with raised arms on a beach at sunset"></div>
  <span class="badge">FEATURED</span>
  <h3>Lorem ipsum dolor sit amet, consectetur adipiscing elit.</h3>
  <div class="meta">John Smith &nbsp; 18/10/2016 &nbsp; 18 Comments</div>
</article>
<article class="mini" style="left:431px;top:737px"><div class="thumb t-lake" role="img" aria-label="Lakeside train journey"></div><h4>Lorem ipsum dolor sit amet, consectetur adipiscing elit.</h4><div class="meta">18/10/2016 &nbsp; 18 Comments</div></article>
<article class="mini" style="left:431px;top:841px"><div class="thumb t-boat" role="img" aria-label="Long-tail boat on a turquoise bay"></div><h4>Lorem ipsum dolor sit amet, consectetur adipiscing elit.</h4><div class="meta">18/10/2016 &nbsp; 18 Comments</div></article>
<article class="mini" style="left:431px;top:945px"><div class="thumb t-field" role="img" aria-label="Traveller in a golden field"></div><h4>Lorem ipsum dolor sit amet, consectetur adipiscing elit.</h4><div class="meta">18/10/2016 &nbsp; 18 Comments</div></article>

<!-- Life style / Medicine block -->
<div class="sec-head" style="--c:var(--red);left:75px;top:1059px;width:343px"><span class="tag">Life Style</span><span class="more">MORE ›</span></div>
<div class="sec-head" style="--c:var(--orange);left:431px;top:1059px;width:343px"><span class="tag">Medicine</span><span class="more">MORE ›</span></div>
<article class="feature" style="left:75px;top:1110px">
  <div class="photo t-curly" role="img" aria-label="Woman with curly hair laughing outdoors"></div>
  <span class="badge">FEATURED</span>
  <h3>Lorem ipsum dolor sit amet, consectetur adipiscing elit.</h3>
  <div class="meta">John Smith &nbsp; 18/10/2016 &nbsp; 18 Comments</div>
</article>
<article class="feature" style="left:431px;top:1110px">
  <div class="photo t-pills" role="img" aria-label="Capsules and pills spilling from a bottle"></div>
  <span class="badge" style="background:var(--green)">FEATURED</span>
  <h3>Lorem ipsum dolor sit amet, consectetur adipiscing elit.</h3>
  <div class="meta">John Smith &nbsp; 18/10/2016 &nbsp; 18 Comments</div>
</article>
<article class="mini narrow" style="left:75px;top:1421px"><div class="thumb t-friends" role="img" aria-label="Friends sitting together"></div><h4>Lorem ipsum dolor sit amet, consectetur adipiscing elit.</h4><div class="meta">18/10/2016 &nbsp; 18 Comments</div></article>
<article class="mini narrow" style="left:75px;top:1525px"><div class="thumb t-friends" role="img" aria-label="Group of friends laughing"></div><h4>Lorem ipsum dolor sit amet, consectetur adipiscing elit.</h4><div class="meta">18/10/2016 &nbsp; 18 Comments</div></article>
<article class="mini narrow" style="left:75px;top:1628px"><div class="thumb t-beach" role="img" aria-label="Car on a coastal road"></div><h4>Lorem ipsum dolor sit amet, consectetur adipiscing elit.</h4><div class="meta">18/10/2016 &nbsp; 18 Comments</div></article>
<article class="mini narrow" style="left:431px;top:1421px"><div class="thumb t-clinic" role="img" aria-label="Doctor in a clinic"></div><h4>Lorem ipsum dolor sit amet, consectetur adipiscing elit.</h4><div class="meta">18/10/2016 &nbsp; 18 Comments</div></article>
<article class="mini narrow" style="left:431px;top:1525px"><div class="thumb t-salad" role="img" aria-label="Bowl of fresh salad"></div><h4>Lorem ipsum dolor sit amet, consectetur adipiscing elit.</h4><div class="meta">18/10/2016 &nbsp; 18 Comments</div></article>
<article class="mini narrow" style="left:431px;top:1628px"><div class="thumb t-field" role="img" aria-label="Yoga pose at sunset"></div><h4>Lorem ipsum dolor sit amet, consectetur adipiscing elit.</h4><div class="meta">18/10/2016 &nbsp; 18 Comments</div></article>

<!-- Recent posts -->
<div class="sec-head" style="--c:var(--cyan);left:75px;top:1746px;width:705px"><span class="tag">Recent Posts</span><span class="more">MORE ›</span></div>
<article class="post" style="top:1796px"><div class="thumb t-boat" role="img" aria-label="Woman in a sun hat by a convertible at the sea"></div><span class="cat" style="background:var(--cyan)">Travel</span><h4>Lorem ipsum dolor sit amet, consectetur adipiscing elit,</h4><div class="meta">John Smith &nbsp; 18/10/2016 &nbsp; 18 Comments</div><p>Lorem ipsum dolor sit amet, consectetur adipiscing elit, sed do eiusmod tempor incididunt ut labore et dolore magna aliqua.</p><span class="read">READ MORE</span></article>
<article class="post" style="top:1972px"><div class="thumb t-bike" role="img" aria-label="Woman riding a bicycle"></div><span class="cat" style="background:var(--red)">Lifestyle</span><h4>Lorem ipsum dolor sit amet, consectetur adipiscing elit,</h4><div class="meta">John Smith &nbsp; 18/10/2016 &nbsp; 18 Comments</div><p>Lorem ipsum dolor sit amet, consectetur adipiscing elit, sed do eiusmod tempor incididunt ut labore et dolore magna aliqua.</p><span class="read">READ MORE</span></article>
<article class="post" style="top:2148px"><div class="thumb t-laptop" role="img" aria-label="Person working on a laptop in a dark room"></div><span class="cat" style="background:var(--green)">Life Hacking</span><h4>Lorem ipsum dolor sit amet, consectetur adipiscing elit,</h4><div class="meta">John Smith &nbsp; 18/10/2016 &nbsp; 18 Comments</div><p>Lorem ipsum dolor sit amet, consectetur adipiscing elit, sed do eiusmod tempor incididunt ut labore et dolore magna aliqua.</p><span class="read">READ MORE</span></article>
<article class="post" style="top:2324px"><div class="thumb t-clinic" role="img" aria-label="Doctor consulting with a patient"></div><span class="cat" style="background:var(--orange)">Medicine</span><h4>Lorem ipsum dolor sit amet, consectetur adipiscing elit,</h4><div class="meta">John Smith &nbsp; 18/10/2016 &nbsp; 18 Comments</div><p>Lorem ipsum dolor sit amet, consectetur adipiscing elit, sed do eiusmod tempor incididunt ut labore et dolore magna aliqua.</p><span class="read">READ MORE</span></article>
<article class="post" style="top:2500px"><div class="thumb t-field" role="img" aria-label="Traveller with a map in a sunny landscape"></div><span class="cat" style="background:var(--cyan)">Travel</span><h4>Lorem ipsum dolor sit amet, consectetur adipiscing elit,</h4><div class="meta">John Smith &nbsp; 18/10/2016 &nbsp; 18 Comments</div><p>Lorem ipsum dolor sit amet, consectetur adipiscing elit, sed do eiusmod tempor incididunt ut labore et dolore magna aliqua.</p><span class="read">READ MORE</span></article>
<div class="pager">‹ &nbsp;NEWER POSTS &nbsp; / &nbsp; OLDER POSTS &nbsp;›</div>

<!-- Travel block (second) -->
<div class="sec-head" style="--c:var(--cyan);left:75px;top:2717px;width:705px"><span class="tag">Travel</span><span class="more">MORE ›</span></div>
<article class="feature" style="left:75px;top:2767px">
  <div class="photo t-beach" role="img" aria-label="Woman with raised arms on a beach at sunset"></div>
  <span class="badge">FEATURED</span>
  <h3>Lorem ipsum dolor sit amet, consectetur adipiscing elit.</h3>
  <div class="meta">John Smith &nbsp; 18/10/2016 &nbsp; 18 Comments</div>
</article>
<article class="mini" style="left:431px;top:2767px"><div class="thumb t-lake" role="img" aria-label="Lakeside train journey"></div><h4>Lorem ipsum dolor sit amet, consectetur adipiscing elit.</h4><div class="meta">18/10/2016 &nbsp; 18 Comments</div></article>
<article class="mini" style="left:431px;top:2871px"><div class="thumb t-boat" role="img" aria-label="Long-tail boat on a turquoise bay"></div><h4>Lorem ipsum dolor sit amet, consectetur adipiscing elit.</h4><div class="meta">18/10/2016 &nbsp; 18 Comments</div></article>
<article class="mini" style="left:431px;top:2975px"><div class="thumb t-field" role="img" aria-label="Traveller in a golden field"></div><h4>Lorem ipsum dolor sit amet, consectetur adipiscing elit.</h4><div class="meta">18/10/2016 &nbsp; 18 Comments</div></article>

<!-- Life style / Medicine block (second) -->
<div class="sec-head" style="--c:var(--red);left:75px;top:3092px;width:343px"><span class="tag">Life Style</span><span class="more">MORE ›</span></div>
<div class="sec-head" style="--c:var(--orange);left:431px;top:3092px;width:343px"><span class="tag">Medicine</span><span class="more">MORE ›</span></div>
<article class="feature" style="left:75px;top:3143px">
  <div class="photo t-curly" role="img" aria-label="Woman with curly hair laughing outdoors"></div>
  <span class="badge">FEATURED</span>
  <h3>Lorem ipsum dolor sit amet, consectetur adipiscing elit.</h3>
  <div class="meta">John Smith &nbsp; 18/10/2016 &nbsp; 18 Comments</div>
</article>
<article class="feature" style="left:431px;top:3143px">
  <div class="photo t-pills" role="img" aria-label="Capsules and pills spilling from a bottle"></div>
  <span class="badge" style="background:var(--green)">FEATURED</span>
  <h3>Lorem ipsum dolor sit amet, consectetur adipiscing elit.</h3>
  <div class="meta">John Smith &nbsp; 18/10/2016 &nbsp; 18 Comments</div>
</article>
<article class="mini narrow" style="left:75px;top:3454px"><div class="thumb t-friends" role="img" aria-label="Friends sitting together"></div><h4>Lorem ipsum dolor sit amet, consectetur adipiscing elit.</h4><div class="meta">18/10/2016 &nbsp; 18 Comments</div></article>
<article class="mini narrow" style="left:75px;top:3558px"><div class="thumb t-friends" role="img" aria-label="Group of friends laughing"></div><h4>Lorem ipsum dolor sit amet, consectetur adipiscing elit.</h4><div class="meta">18/10/2016 &nbsp; 18 Comments</div></article>
<article class="mini narrow" style="left:75px;top:3661px"><div class="thumb t-beach" role="img" aria-label="Car on a coastal road"></div><h4>Lorem ipsum dolor sit amet, consectetur adipiscing elit.</h4><div class="meta">18/10/2016 &nbsp; 18 Comments</div></article>
<article class="mini narrow" style="left:431px;top:3454px"><div class="thumb t-clinic" role="img" aria-label="Doctor in a clinic"></div><h4>Lorem ipsum dolor sit amet, consectetur adipiscing elit.</h4><div class="meta">18/10/2016 &nbsp; 18 Comments</div></article>
<article class="mini narrow" style="left:431px;top:3558px"><div class="thumb t-salad" role="img" aria-label="Bowl of fresh salad"></div><h4>Lorem ipsum dolor sit amet, consectetur adipiscing elit.</h4><div class="meta">18/10/2016 &nbsp; 18 Comments</div></article>
<article class="mini narrow" style="left:431px;top:3661px"><div class="thumb t-field" role="img" aria-label="Yoga pose at sunset"></div><h4>Lorem ipsum dolor sit amet, consectetur adipiscing elit.</h4><div class="meta">18/10/2016 &nbsp; 18 Comments</div></article>

<!-- Sidebar -->
<div class="sec-head" style="--c:var(--cyan);left:793px;top:687px;width:333px"><span class="tag">About Us</span></div>
<aside class="side-box about">
  <div class="avatar" role="img" aria-label="Portrait of the blog author"></div>
  <p>Lorem ipsum dolor sit amet, consectetur adipiscing elit, sed do eiusmod tempor incididunt ut labore et dolore magna aliqua. Ut enim ad minim veniam, quis nostrud exercitation ullamco laboris nisi ut aliquip ex ea commodo consequat. Duis aute irure dolor in reprehenderit.</p>
  <span class="btn">READ MORE</span>
</aside>

<div class="sec-head" style="--c:var(--cyan);left:793px;top:1163px;width:333px"><span class="tag">Keep In Touch</span></div>
<div class="social-grid">
  <div style="background:#3b5998"><b>1200</b>Fans</div>
  <div style="background:#55acee"><b>14</b>Followers</div>
  <div style="background:#e52d27"><b>4500</b>Subscribers</div>
  <div style="background:#1ab7ea"><b>1</b>Subscribers</div>
  <div style="background:#ea4c89"><b>100</b>Followers</div>
  <div style="background:#f26522"><b>Subscribe</b>To RSS Feed</div>
</div>

<aside class="ad">
  <div class="watch" role="img" aria-label="Red wooden wristwatch"></div>
  <div class="kicker">LUXURY</div>
  <div class="title">WOOD<br>WATCHES</div>
  <div class="name">TIMBRA</div>
  <span class="shop">SHOP NOW</span>
  <div class="url">timbrawatches.com</div>
</aside>

<div class="sec-head" style="--c:var(--cyan);left:793px;top:1756px;width:333px"><span class="tag">Newsletter!</span></div>
<aside class="side-box news">
  <p>Subscribe my Newsletter for new recipes, right from your inbox. Let's stay updated!</p>
  <div class="field" style="top:70px">Name</div>
  <div class="field" style="top:116px">Email</div>
  <div class="sub">SUBSCRIBE NOW</div>
</aside>

<div class="sec-head" style="--c:var(--cyan);left:793px;top:2044px;width:333px"><span class="tag">Tweets</span></div>
<aside class="side-box tweets">
  <svg class="bird" width="34" height="34" viewBox="0 0 34 34"><circle cx="17" cy="17" r="15" fill="var(--cyan)"/></svg>
  <p>#Blog and #Magazine with 900+ #Demo #Homepages. Get it now: <span class="link">https://brnx.link/4kQ2mT</span></p>
  <div class="date">September 1, 2016</div>
  <div class="acts">Reply &nbsp;|&nbsp; Retweet &nbsp;|&nbsp; Favorite</div>
  <div class="dots"><i></i><i></i><i></i><i></i><i></i></div>
</aside>

<div class="sec-head" style="--c:var(--cyan);left:793px;top:2360px;width:333px"><span class="tag">Archive</span></div>
<ul class="side-box archive">
  <li>May 2016</li><li>April 2015</li><li>January 2014</li><li>April 2014</li><li>March 2014</li><li>February 2014</li>
</ul>

<div class="sec-head" style="--c:var(--cyan);left:793px;top:2656px;width:333px"><span class="tag">Snapfeed</span></div>
<aside class="side-box photo-feed">
  <div class="grid">
    <div class="t-beach" role="img" aria-label="Travel photo"></div>
    <div class="t-friends" role="img" aria-label="Friends photo"></div>
    <div class="t-salad" role="img" aria-label="Food photo"></div>
    <div class="t-curly" role="img" aria-label="Lifestyle photo"></div>
    <div class="t-lake" role="img" aria-label="Lake photo"></div>
    <div class="t-boat" role="img" aria-label="Beach photo"></div>
    <div class="t-couple" role="img" aria-label="Couple photo"></div>
    <div class="t-field" role="img" aria-label="Field photo"></div>
    <div class="t-pills" role="img" aria-label="Medicine photo"></div>
    <div class="t-bike" role="img" aria-label="Cycling photo"></div>
    <div class="t-mountain" role="img" aria-label="Mountain photo"></div>
    <div class="t-clinic" role="img" aria-label="Clinic photo"></div>
  </div>
  <div class="btn">Follow Us On Snapfeed</div>
</aside>

<footer class="footer">
  <nav>Home<span>/</span>About Us<span>/</span>Travel<span>/</span>Lifestyle<span>/</span>Life Hacking<span>/</span>Medicine<span>/</span>Contact</nav>
  <div class="icons"><i></i><i></i><i></i><i></i><i></i><i></i><i></i></div>
  <div class="copy">Copyright ©2016 All Rights Reserved. Terms of Use | Privacy Policy</div>
</footer>

</body>
</html>
```